Building company with a modern and unique product looking for a business card to help us stand out

We currently have a logo but as our business has grown, we feel that our business card is not reflecting our modern and high quality product and help us stand out from the crowd. Our business is mainly in the construction of new homes using a unique method and materials that makes our homes fire proof, vermin and pest resistant and rated to the maximum cyclone category (category 5). We need a business card that helps us stand out as well as communicating professionalism, high quality and trustworthiness. I have attached our current logo with a black and white option, as well as our business card which is double sided. We would like to retain as much of the information that is currently on our business cards, but presented in a more sleek way. We do like our current colour palette ( white, black, yellow and grey) and have been looking primarily at business cards with a black background however we are open to other combinations of colour and layout as long as we stand out. Please feel free to tweak our logo to make it more suitable for a business card, we like the black option that we use but we have had trouble trying to get the white area to match the rest of the logo and blend effectively into a business card. Please do not hesitate to contact us with any questions as we really want this to be successful!

Target Market(s)

Large contracts including government and larger companies

Industry/Entity Type

Business

We will be providing this business card to potential clients including key government ministers and large funding companies, our business card should show that we are professional and reliable.

Requirements
Must have
• It must be easy to read and pleasing to the eye, It must contain as much of the information on the current business card and unless something really stands out, we will most likely pick a design that has all of the information included. It must include our logo of course and have some colour included.
Nice to have
• We are looking for a high end business card and would like to see designs that reflect this. We like the gloss/matte contrast, plastic cards with opaque/coloured areas and unique features not seen on everyday paper business cards. It would be nice to see a few different colour combinations, we are open to new ideas so please feel free to take some artistic licence.
Should not have
• Must not be too busy, difficult to read or be distracting from the information conveyed. Other than this please feel free to add your own touches and make it unique!

```html
<!DOCTYPE html>
<html lang="en">
<head>
<meta charset="utf-8">
<title>Kestrel Building Company – Business Card</title>
<link rel="stylesheet" href="https://fonts.googleapis.com/css2?family=Montserrat:wght@400;500&display=swap">
<style>
  :root {
    --stage: #3b3431;
    --card: #141414;
    --white: #f2f2f2;
    --gold: #c9a227;
    --grey: #8a8a8a;
  }
  * { margin: 0; padding: 0; box-sizing: border-box; }
  html, body { width: 1200px; height: 780px; overflow: hidden; }
  body {
    background: var(--stage);
    font-family: "Montserrat", sans-serif;
    display: flex;
    align-items: center;
    justify-content: center;
    gap: 40px;
  }
  .card {
    position: relative;
    width: 540px;
    height: 309px;
    background: var(--card);
    border-radius: 6px;
    box-shadow: 0 10px 30px rgba(0,0,0,.45);
    color: var(--white);
  }
  .brand {
    position: absolute;
    display: flex;
    align-items: center;
    gap: 10px;
    font-weight: 500;
    color: var(--white);
    line-height: 1.15;
  }
  .brand-mark {
    width: 14px;
    height: 14px;
    background: var(--gold);
    flex: none;
  }
  .brand-name { font-size: 19px; letter-spacing: .5px; }

  /* Front */
  .card-front .brand { top: 62px; left: 190px; }
  .person {
    position: absolute;
    top: 168px;
    left: 40px;
  }
  .person-name { font-size: 19px; letter-spacing: .3px; }
  .person-title { font-size: 13px; color: var(--gold); margin-top: 4px; }
  .divider {
    position: absolute;
    width: 1.5px;
    background: var(--white);
  }
  .card-front .divider { top: 172px; left: 236px; height: 56px; }
  .contact {
    position: absolute;
    top: 170px;
    left: 252px;
    list-style: none;
    font-size: 12.5px;
    line-height: 20px;
  }
  .contact-label { color: var(--gold); margin-right: 4px; }

  /* Back */
  .card-back .brand { top: 70px; left: 250px; }
  .tagline {
    position: absolute;
    top: 180px;
    left: 40px;
    font-size: 18px;
    line-height: 26px;
    color: var(--gold);
  }
  .card-back .divider { top: 184px; left: 250px; height: 52px; }
  .features {
    position: absolute;
    top: 180px;
    left: 266px;
    list-style: none;
    font-size: 14px;
    line-height: 19px;
  }
</style>
</head>
<body>
  <section class="card card-front" aria-label="Business card front">
    <div class="brand">
      <span class="brand-mark"></span>
      <span class="brand-name">Kestrel Building<br>Company</span>
    </div>
    <div class="person">
      <p class="person-name">Daniel Whitford</p>
      <p class="person-title">Managing Director</p>
    </div>
    <span class="divider"></span>
    <ul class="contact">
      <li><span class="contact-label">C:</span>0400 555 019</li>
      <li><span class="contact-label">O:</span>(02) 5550 1234</li>
      <li><span class="contact-label">E:</span>info@kestrelbuilding.example</li>
    </ul>
  </section>

  <section class="card card-back" aria-label="Business card back">
    <div class="brand">
      <span class="brand-mark"></span>
      <span class="brand-name">Kestrel Building<br>Company</span>
    </div>
    <p class="tagline">Specialising in<br>Homes that are</p>
    <span class="divider"></span>
    <ul class="features">
      <li>Fire Proof</li>
      <li>Climate Proof</li>
      <li>Cyclone Rated(cat.5)</li>
    </ul>
  </section>
</body>
</html>
```